Business Card Design

Freelance writer, coach, teacher and researcher specialising in improving mathematics teaching and learning in primary schools. I write books and articles for teachers, speak extensively at conferences in UK and aboard. Would like something with a cube in the design. Clean, modern - logo suitable for use on a website. Should NOT look 'childish' (no comic sans or chalkboard type fonts)

Full details to go on card:

Professor Dan Theroll
Unlocking Early Numeracy

info@dantheroll.net
#dantheroll26
www.dantheroll.net
+44 7812 660 394

Industry/Entity Type

Teacher

Contact Information for Business Card

Professor Dan Theroll
Unlocking Early Numbers

```html
<!DOCTYPE html>
<html lang="en">
<head>
<meta charset="utf-8">
<title>Dan Theroll – Business Card Colour Options</title>
<link rel="stylesheet" href="https://fonts.googleapis.com/css2?family=Arimo:wght@400;700&family=Noto+Serif:wght@400;700&display=swap">
<style>
  :root {
    --sheet-bg: #ffffff;
    --label-ink: #111111;
    --green: #356a33;
    --purple: #3d2e7c;
    --blue: #2c3a8c;
    --charcoal: #333333;
    --bar-ink: #ffffff;
    --divider: rgba(255, 255, 255, 0.55);
    --rule: #c9c9c9;
  }
  * { box-sizing: border-box; margin: 0; padding: 0; }
  html, body { width: 1200px; height: 702px; overflow: hidden; background: var(--sheet-bg); }
  .sheet { position: relative; width: 1200px; height: 702px; }

  .option-label {
    position: absolute;
    font-family: "Arimo", Arial, sans-serif;
    font-size: 38px;
    color: var(--label-ink);
    line-height: 1;
  }

  .card {
    position: absolute;
    width: 487px;
    height: 307px;
    color: var(--accent);
  }
  .card--green { --accent: var(--green); left: 60px; top: 24px; }
  .card--purple { --accent: var(--purple); left: 679px; top: 20px; }
  .card--blue { --accent: var(--blue); left: 62px; top: 376px; }
  .card--charcoal { --accent: var(--charcoal); left: 690px; top: 376px; }

  .card__top-bar {
    position: absolute; left: 0; top: 0;
    width: 483px; height: 27px;
    background: var(--accent);
  }

  .card__mark {
    position: absolute; left: 0; top: 42px;
    width: 483px; height: 134px;
    display: flex; align-items: center; justify-content: center; gap: 10px;
  }
  .card__mark-square {
    width: 22px; height: 22px; background: var(--accent);
  }
  .card__mark-name {
    font-family: "Noto Serif", Georgia, serif;
    font-weight: 700;
    font-size: 24px;
    color: var(--accent);
  }

  .card__name {
    position: absolute; left: 0; top: 193px; width: 483px;
    text-align: center;
    font-family: "Noto Serif", Georgia, serif;
    font-weight: 700;
    font-size: 15.5px;
    letter-spacing: 0.3px;
    color: var(--accent);
  }
  .card__rule {
    position: absolute; left: 164px; top: 216px;
    width: 155px; height: 1px; background: var(--rule);
  }
  .card__tagline {
    position: absolute; left: 0; top: 221px; width: 483px;
    text-align: center;
    font-family: "Arimo", Arial, sans-serif;
    font-weight: 700;
    font-size: 8.6px;
    color: var(--accent);
  }

  .card__contact-bar {
    position: absolute; left: 0; top: 254px;
    width: 487px; height: 53px;
    background: var(--accent);
    display: flex;
    color: var(--bar-ink);
    font-family: "Noto Serif", Georgia, serif;
    font-size: 8.4px;
    letter-spacing: 0.6px;
  }
  .contact {
    display: flex; align-items: center; gap: 10px;
    padding-left: 12px;
    border-right: 1px solid var(--divider);
  }
  .contact:last-child { border-right: none; }
  .contact--phone { width: 160px; }
  .contact--social { width: 163px; padding-left: 16px; }
  .contact--web { flex: 1; padding-left: 12px; line-height: 1.35; }
  .contact__icon { width: 18px; height: 18px; flex: none; }
  .contact__network { font-family: "Noto Serif", Georgia, serif; }
  .contact__dot { width: 9px; height: 9px; border-radius: 50%; background: var(--bar-ink); flex: none; }
</style>
</head>
<body>
<main class="sheet">

  <span class="option-label" style="left:64px; top:136px;">A</span>
  <span class="option-label" style="left:700px; top:139px;">C</span>
  <span class="option-label" style="left:55px; top:491px;">B</span>
  <span class="option-label" style="left:694px; top:491px;">D</span>

  <!-- Option A -->
  <section class="card card--green">
    <div class="card__top-bar"></div>
    <div class="card__mark"><span class="card__mark-square"></span><span class="card__mark-name">Dan Theroll</span></div>
    <h1 class="card__name">Professor Dan Theroll</h1>
    <div class="card__rule"></div>
    <p class="card__tagline">Unlocking Early Numeracy</p>
    <div class="card__contact-bar">
      <div class="contact contact--phone">
        <svg class="contact__icon" viewBox="0 0 24 24"><path fill="currentColor" d="M8 2c-1.5 0-3 1.5-3 4v12c0 2.5 1.5 4 3 4h2l1-6-2.5-1V9L11 8l-1-6z"/></svg>
        <span>+44 (7812) 660 394</span>
      </div>
      <div class="contact contact--social">
        <span class="contact__dot"></span>
        <span><span class="contact__network">Chirper</span> dantheroll26</span>
      </div>
      <div class="contact contact--web">
        <svg class="contact__icon" viewBox="0 0 24 24" fill="none" stroke="currentColor" stroke-width="1.3"><circle cx="12" cy="12" r="10"/><ellipse cx="12" cy="12" rx="4.5" ry="10"/><path d="M2 12h20M4 6.5h16M4 17.5h16M12 2v20"/></svg>
        <span>info@dantheroll.net<br>www.dantheroll.net</span>
      </div>
    </div>
  </section>

  <!-- Option C -->
  <section class="card card--purple">
    <div class="card__top-bar"></div>
    <div class="card__mark"><span class="card__mark-square"></span><span class="card__mark-name">Dan Theroll</span></div>
    <h1 class="card__name">Professor Dan Theroll</h1>
    <div class="card__rule"></div>
    <p class="card__tagline">Unlocking Early Numeracy</p>
    <div class="card__contact-bar">
      <div class="contact contact--phone">
        <svg class="contact__icon" viewBox="0 0 24 24"><path fill="currentColor" d="M8 2c-1.5 0-3 1.5-3 4v12c0 2.5 1.5 4 3 4h2l1-6-2.5-1V9L11 8l-1-6z"/></svg>
        <span>+44 (7812) 660 394</span>
      </div>
      <div class="contact contact--social">
        <span class="contact__dot"></span>
        <span><span class="contact__network">Chirper</span> dantheroll26</span>
      </div>
      <div class="contact contact--web">
        <svg class="contact__icon" viewBox="0 0 24 24" fill="none" stroke="currentColor" stroke-width="1.3"><circle cx="12" cy="12" r="10"/><ellipse cx="12" cy="12" rx="4.5" ry="10"/><path d="M2 12h20M4 6.5h16M4 17.5h16M12 2v20"/></svg>
        <span>info@dantheroll.net<br>www.dantheroll.net</span>
      </div>
    </div>
  </section>

  <!-- Option B -->
  <section class="card card--blue">
    <div class="card__top-bar"></div>
    <div class="card__mark"><span class="card__mark-square"></span><span class="card__mark-name">Dan Theroll</span></div>
    <h1 class="card__name">Professor Dan Theroll</h1>
    <div class="card__rule"></div>
    <p class="card__tagline">Unlocking Early Numeracy</p>
    <div class="card__contact-bar">
      <div class="contact contact--phone">
        <svg class="contact__icon" viewBox="0 0 24 24"><path fill="currentColor" d="M8 2c-1.5 0-3 1.5-3 4v12c0 2.5 1.5 4 3 4h2l1-6-2.5-1V9L11 8l-1-6z"/></svg>
        <span>+44 (7812) 660 394</span>
      </div>
      <div class="contact contact--social">
        <span class="contact__dot"></span>
        <span><span class="contact__network">Chirper</span> dantheroll26</span>
      </div>
      <div class="contact contact--web">
        <svg class="contact__icon" viewBox="0 0 24 24" fill="none" stroke="currentColor" stroke-width="1.3"><circle cx="12" cy="12" r="10"/><ellipse cx="12" cy="12" rx="4.5" ry="10"/><path d="M2 12h20M4 6.5h16M4 17.5h16M12 2v20"/></svg>
        <span>info@dantheroll.net<br>www.dantheroll.net</span>
      </div>
    </div>
  </section>

  <!-- Option D -->
  <section class="card card--charcoal">
    <div class="card__top-bar"></div>
    <div class="card__mark"><span class="card__mark-square"></span><span class="card__mark-name">Dan Theroll</span></div>
    <h1 class="card__name">Professor Dan Theroll</h1>
    <div class="card__rule"></div>
    <p class="card__tagline">Unlocking Early Numeracy</p>
    <div class="card__contact-bar">
      <div class="contact contact--phone">
        <svg class="contact__icon" viewBox="0 0 24 24"><path fill="currentColor" d="M8 2c-1.5 0-3 1.5-3 4v12c0 2.5 1.5 4 3 4h2l1-6-2.5-1V9L11 8l-1-6z"/></svg>
        <span>+44 (7812) 660 394</span>
      </div>
      <div class="contact contact--social">
        <span class="contact__dot"></span>
        <span><span class="contact__network">Chirper</span> dantheroll26</span>
      </div>
      <div class="contact contact--web">
        <svg class="contact__icon" viewBox="0 0 24 24" fill="none" stroke="currentColor" stroke-width="1.3"><circle cx="12" cy="12" r="10"/><ellipse cx="12" cy="12" rx="4.5" ry="10"/><path d="M2 12h20M4 6.5h16M4 17.5h16M12 2v20"/></svg>
        <span>info@dantheroll.net<br>www.dantheroll.net</span>
      </div>
    </div>
  </section>

</main>
</body>
</html>
```